B Orme Artist Business Card

I need a business card for myself working as an emerging artist. I have an artwork that has been exhibited at an Awards exhibition that I would like incorporated into my business card. The card needs to be simple but different so I was thinking about one that is perhaps half or 1/3 of the normal business card size so that it could be slipped comfortably into little pouches. I only want my name, email, mobile number and facebook artist page link on the card.Perhaps the artwork on the size of a normal business card and then the card chopped up into 3 so that I have 3 business cards of different look and my details on the blank side of the card..unless someone can come up with a more interesting concept that is simple and fit for an emerging artist :)

```html
<!DOCTYPE html>
<html lang="en">
<head>
<meta charset="utf-8">
<title>B Orme Artist – Business Card</title>
<link rel="stylesheet" href="https://fonts.googleapis.com/css2?family=Cinzel:wght@400;600&display=swap">
<style>
  :root {
    --page-bg: #ecebe8;
    --card-white: #ffffff;
    --orange: #e8843a;
    --orange-light: #f39a4a;
    --rust: #b8401e;
    --deep-red: #8e1f12;
    --sky: #1aa0dc;
    --navy: #1d3566;
    --ink-grey: #6b6b6b;
    --icon-grey: #8a8d93;
  }
  * { box-sizing: border-box; margin: 0; padding: 0; }
  html, body {
    width: 1200px; height: 727px; overflow: hidden;
    background: var(--page-bg);
  }
  .canvas { position: relative; width: 1200px; height: 727px; }
  .card {
    position: absolute; top: 209px;
    width: 540px; height: 309px;
    overflow: hidden;
    box-shadow: 0 4px 14px rgba(0,0,0,0.18);
  }
  .card--front { left: 40px; background: var(--card-white); }
  .card--back {
    left: 620px;
    background: radial-gradient(ellipse at 52% 55%, var(--orange-light) 0%, #d9662c 45%, var(--rust) 80%, var(--deep-red) 100%);
  }
  .brand {
    font-family: "Cinzel", serif;
    font-weight: 400;
    white-space: nowrap;
    text-align: center;
    letter-spacing: 1px;
    line-height: 1;
  }
  .card--front .brand {
    position: absolute; top: 30px; left: 0; width: 100%;
    font-size: 42px; color: var(--orange);
  }
  .card--back .brand {
    position: absolute; top: 50%; left: 0; width: 100%;
    transform: translateY(-50%);
    font-size: 46px; color: #fff;
  }
  .person {
    position: absolute; top: 118px; right: 290px;
    text-align: right; font-family: "Cinzel", serif;
  }
  .person__name { color: var(--orange); font-size: 15px; font-weight: 600; letter-spacing: .5px; }
  .person__role { color: var(--sky); font-size: 13px; letter-spacing: .5px; }
  .divider {
    position: absolute; left: 266px; top: 96px;
    width: 1px; height: 86px; background: var(--orange);
  }
  .contacts {
    position: absolute; left: 282px; top: 100px;
    list-style: none; font-family: "Cinzel", serif;
    font-size: 11.5px; color: var(--ink-grey); letter-spacing: .3px;
  }
  .contacts li { display: flex; align-items: center; height: 17px; }
  .contacts .dot {
    width: 9px; height: 9px; border-radius: 50%;
    background: var(--icon-grey); margin-right: 6px; flex: none;
  }
  .swoosh { position: absolute; left: 0; top: 0; }
</style>
</head>
<body>
<main class="canvas">
  <section class="card card--front" aria-label="Card front">
    <svg class="swoosh" width="540" height="309" viewBox="0 0 540 309" aria-hidden="true">
      <defs>
        <radialGradient id="swooshFill" cx="0.45" cy="0.75" r="0.7">
          <stop offset="0" stop-color="#f08a3a"/>
          <stop offset="0.6" stop-color="#c4501f"/>
          <stop offset="1" stop-color="#8e1f12"/>
        </radialGradient>
      </defs>
      <path d="M0,309 L0,292 C120,250 230,215 330,205 C420,196 480,170 540,150 L540,309 Z" fill="url(#swooshFill)"/>
      <path d="M0,288 C120,244 230,210 330,199 C420,190 480,164 540,144" fill="none" stroke="#1aa0dc" stroke-width="3"/>
      <path d="M0,281 C120,237 230,203 330,192 C420,183 480,157 540,137" fill="none" stroke="#1d3566" stroke-width="2.5"/>
    </svg>
    <h1 class="brand">B Orme Artist</h1>
    <div class="person">
      <p class="person__name">Bea Orme</p>
      <p class="person__role">Emerging Artist</p>
    </div>
    <div class="divider"></div>
    <ul class="contacts">
      <li><span class="dot"></span>07700 900 415</li>
      <li><span class="dot"></span>0117 496 0821</li>
      <li><span class="dot"></span>HELLO@ORMESTUDIO.COM</li>
      <li><span class="dot"></span>WWW.ORMESTUDIO.COM</li>
    </ul>
  </section>

  <section class="card card--back" aria-label="Card back">
    <h2 class="brand">B Orme Artist</h2>
  </section>
</main>
</body>
</html>
```